A empresa queria:
" Pista de Tiro indoor, pessoas pagam por ano ou por visita aluguel de pista de tiro aluguel de arma venda de arma venda de munição cursos de tiro Documentação para aquisição de arma CAÇA DE JAVALI "

```html
<!DOCTYPE html>
<html lang="pt-BR">
<head>
<meta charset="utf-8">
<title>Ronaldo Siqueira – Capa da Página</title>
<link href="https://fonts.googleapis.com/css2?family=Montserrat:wght@400;600;700;800&display=swap" rel="stylesheet">
<style>
  :root {
    --canvas: #eceded;
    --charcoal: #1f1f21;
    --charcoal-deep: #151516;
    --brand-red: #d3121b;
    --ink: #1b1b1b;
    --white: #ffffff;
    --photo-light: #e9e9e9;
    --photo-mid: #c9cbcd;
  }
  * { box-sizing: border-box; margin: 0; padding: 0; }
  html, body { width: 1200px; height: 1200px; overflow: hidden; }
  body {
    background: var(--canvas);
    font-family: "Montserrat", Arial, sans-serif;
    position: relative;
  }

  .brand-lockup {
    display: flex; align-items: center; gap: 14px;
  }
  .brand-square {
    flex: none;
    width: 18px; height: 18px;
    background: var(--brand-red);
  }
  .brand-name {
    color: var(--white); font-weight: 700; white-space: nowrap;
  }

  /* Profile picture */
  .profile-picture {
    position: absolute;
    left: 50px; top: 220px;
    width: 300px; height: 300px;
    background: var(--charcoal);
    display: flex; align-items: center; justify-content: center;
  }
  .profile-picture .brand-name { font-size: 26px; }

  /* Cover */
  .cover {
    position: absolute;
    left: 50px; top: 560px;
    width: 1100px; height: 420px;
    overflow: hidden;
  }
  .cover-shapes { position: absolute; inset: 0; }

  .cover-brand {
    position: absolute;
    left: 0; top: 0; width: 470px; height: 420px;
    display: flex; flex-direction: column; align-items: center; justify-content: center;
  }
  .cover-brand .brand-square { width: 24px; height: 24px; }
  .cover-brand .brand-name { font-size: 38px; }
  .cover-brand .brand-tagline {
    color: var(--white); font-weight: 600; font-size: 15px; letter-spacing: 2px; margin-top: 14px;
  }

  .services {
    position: absolute;
    right: 40px; top: 34px;
    list-style: none; text-align: right;
  }
  .services li {
    color: var(--ink); font-weight: 700; font-size: 25px; line-height: 1.22;
  }
  .services li::after {
    content: ""; display: inline-block;
    width: 9px; height: 9px; border-radius: 50%;
    background: var(--brand-red); margin-left: 12px; vertical-align: middle;
  }
  .services li.no-dot::after { visibility: hidden; }

  .phone-button {
    position: absolute;
    right: 40px; bottom: 28px;
    background: var(--brand-red); color: var(--white);
    font-weight: 700; font-size: 26px;
    padding: 12px 34px;
    display: flex; align-items: center; gap: 12px;
  }
  .phone-button svg { width: 24px; height: 24px; }
</style>
</head>
<body>

  <div class="profile-picture">
    <div class="brand-lockup">
      <span class="brand-square"></span>
      <span class="brand-name">Ronaldo Siqueira</span>
    </div>
  </div>

  <section class="cover">
    <svg class="cover-shapes" viewBox="0 0 1100 420" width="1100" height="420">
      <defs>
        <linearGradient id="range-tones" x1="0" y1="0" x2="1" y2="1">
          <stop offset="0" stop-color="#c9cbcd"/>
          <stop offset="0.6" stop-color="#e9e9e9"/>
          <stop offset="1" stop-color="#f5f5f5"/>
        </linearGradient>
      </defs>
      <rect role="img" aria-label="Foto clara de uma pista de tiro indoor" x="400" y="0" width="700" height="420" fill="url(#range-tones)"/>
      <polygon points="0,0 520,0 430,420 0,420" fill="#1f1f21"/>
      <polygon points="520,0 560,0 470,420 430,420" fill="#d3121b"/>
      <polygon points="0,0 60,0 0,60" fill="#151516"/>
    </svg>

    <div class="cover-brand">
      <div class="brand-lockup">
        <span class="brand-square"></span>
        <span class="brand-name">Ronaldo Siqueira</span>
      </div>
      <span class="brand-tagline">DESPACHANTE DE ARMAS</span>
    </div>

    <ul class="services">
      <li>Pista de Tiro Indoor</li>
      <li>Aluguel &amp; Venda de Armas</li>
      <li>Venda de Munições</li>
      <li>Cursos de Tiro</li>
      <li class="no-dot">Documentação</li>
      <li>para aquisição de arma</li>
      <li>Caça de Animais Legal</li>
    </ul>

    <div class="phone-button">
      <svg viewBox="0 0 24 24" fill="#ffffff" aria-hidden="true">
        <path d="M6.6 10.8a15.1 15.1 0 0 0 6.6 6.6l2.2-2.2a1 1 0 0 1 1-.25 11.4 11.4 0 0 0 3.6.57 1 1 0 0 1 1 1V20a1 1 0 0 1-1 1A17 17 0 0 1 3 4a1 1 0 0 1 1-1h3.5a1 1 0 0 1 1 1c0 1.25.2 2.45.57 3.57a1 1 0 0 1-.25 1z"/>
      </svg>
      <span>(00) 0000-0000</span>
    </div>
  </section>

</body>
</html>
```